Business Card: RW Office Partners - Your tidy answer finder

Business Name: RW Office Partners
Website: www.rwofficepartners.com.au
Email: marisol@rwofficepartners.com.au
Mobile: 61 487 902 346
Facebook: @rwofficepartners
Instrgram: @rwofficepartners

Brading Colours:
HEX
#986474
#ddccd3
#7a8498
#c9d8e4
#000000
#ffffff

Tag Line: Your tidy answer finder

Link to DRAFT website:
https://helpdeskhub.sitebuilderx.com/rw-office-partners

About Page from the website:
My name is Marisol Bramwell, and I would love to assist you to become more productive in your day to day and achieve your business and personal goals.
My mission is to give you time, time to work on the important tasks of your business or to be able to spend more time with your family. I will take on the tasks you don’t have time for, don’t know well or simply don’t like to do.
I have an extensive background in Administration, Tender Coordination, Document Control, WHS and Quality Management working primarily in the Construction, Mining and Corporate World.
I am passionate about being organised, having order and making things in your life (and mine) easier! I love to watch something unfold and grow into something amazing! I am known for being the go-to problem solver, the organiser of all things, producing high standards of work even under pressure. I’m also a confident communicator, and I understand that you’re busy running your business.

Target Market(s)

Small to Medium Business who require assistance in their business by a virtual assistant.

Industry/Entity Type

Virtual Assistant

Contact Information for Business Card

Mobile: 61 487 902 346

Font styles to use
Sans Serif

Colors
ffffff

Requirements
Must have
• Branding Colours as outlined.
Contact Details as outlined.
Logo as provided.
Proper contact details - mobile, facebook, instragm, website.
Simple, Elegant, very clean looking.
Should not have
• Note cute with pictures.
Not too girly as still want to market to construction companies.

```html
<!DOCTYPE html>
<html lang="en">
<head>
<meta charset="utf-8">
<title>RW Office Partners – Business Card</title>
<link rel="stylesheet" href="https://fonts.googleapis.com/css2?family=Montserrat:wght@500;600&family=Arimo:wght@400&display=swap">
<style>
  :root {
    --plum: #986474;
    --blush: #ddccd3;
    --slate: #7a8498;
    --ice: #c9d8e4;
    --black: #000000;
    --white: #ffffff;
    --page: #c4c4c4;
    --ink: #1a1a1a;
  }
  * { margin: 0; padding: 0; box-sizing: border-box; }
  html, body {
    width: 1100px; height: 1200px; overflow: hidden;
    background: var(--page);
  }
  .canvas {
    position: relative; width: 1100px; height: 1200px;
  }
  .card {
    position: absolute; left: 100px; width: 900px; height: 514px;
    overflow: hidden;
  }
  .card--front { top: 56px; background: radial-gradient(ellipse 60% 70% at 45% 35%, #2b2b2b 0%, #111 55%, var(--black) 100%); }
  .card--back { top: 630px; background: var(--white); }

  .rule { position: absolute; height: 3px; }
  .card--front .rule { background: var(--blush); top: 258px; }
  .card--front .rule--left { left: 0; width: 232px; }
  .card--front .rule--right { right: 0; width: 228px; }

  .wordmark {
    position: absolute; display: flex; align-items: center; gap: 16px;
    font-family: "Montserrat", sans-serif; font-weight: 600;
    text-transform: uppercase; line-height: 1.02; letter-spacing: 0.5px;
  }
  .wordmark__square { width: 18px; height: 18px; flex: none; }
  .wordmark__name { display: block; font-size: 38px; }

  .card--front .wordmark { left: 252px; top: 212px; color: var(--ice); }
  .card--front .wordmark__square { background: var(--ice); }

  .tagline {
    position: absolute; left: 0; right: 0; top: 335px; text-align: center;
    font-family: "Montserrat", sans-serif; font-weight: 600; font-size: 14px;
    letter-spacing: 2.6px; text-transform: uppercase; color: var(--white);
  }

  .socials {
    position: absolute; top: 460px; left: 0; right: 0;
    display: flex; justify-content: center; gap: 62px;
  }
  .social {
    display: flex; align-items: center; gap: 10px;
    font-family: "Montserrat", sans-serif; font-weight: 500; font-size: 16px;
    letter-spacing: 2.4px; color: var(--white);
  }
  .social__dot {
    width: 20px; height: 20px; border: 1.5px solid var(--white); border-radius: 50%;
  }

  .card--back .wordmark { left: 26px; top: 204px; color: var(--slate); }
  .card--back .wordmark__square { background: var(--slate); }
  .card--back .rule { background: var(--plum); top: 252px; left: 466px; right: 0; }

  .contacts {
    position: absolute; left: 107px; top: 330px; list-style: none;
  }
  .contact {
    display: flex; align-items: center; gap: 14px; height: 54px;
    font-family: "Arimo", sans-serif; font-size: 20px; letter-spacing: 0.4px; color: var(--ink);
  }
  .contact__icon {
    width: 34px; height: 34px; border-radius: 50%; background: var(--slate);
    display: flex; align-items: center; justify-content: center; flex: none;
  }
  .contact__icon svg { width: 20px; height: 20px; }
</style>
</head>
<body>
<main class="canvas">

  <section class="card card--front" aria-label="Business card front">
    <div class="rule rule--left"></div>
    <div class="rule rule--right"></div>
    <div class="wordmark">
      <span class="wordmark__square"></span>
      <span><span class="wordmark__name">RW Office</span><span class="wordmark__name">Partners</span></span>
    </div>
    <p class="tagline">Your tidy answer finder</p>
    <div class="socials">
      <span class="social"><span class="social__dot"></span>@rwofficepartners</span>
      <span class="social"><span class="social__dot"></span>@rwofficepartners</span>
    </div>
  </section>

  <section class="card card--back" aria-label="Business card back">
    <div class="wordmark">
      <span class="wordmark__square"></span>
      <span><span class="wordmark__name">RW Office</span><span class="wordmark__name">Partners</span></span>
    </div>
    <div class="rule"></div>
    <ul class="contacts">
      <li class="contact">
        <span class="contact__icon">
          <svg viewBox="0 0 20 20" fill="none" stroke="#fff" stroke-width="1.2">
            <circle cx="10" cy="10" r="8"/><ellipse cx="10" cy="10" rx="3.5" ry="8"/>
            <line x1="2" y1="10" x2="18" y2="10"/><path d="M3.5 6h13M3.5 14h13"/>
          </svg>
        </span>
        www.rwofficepartners.com.au
      </li>
      <li class="contact">
        <span class="contact__icon">
          <svg viewBox="0 0 20 20" fill="none" stroke="#fff" stroke-width="1.2">
            <rect x="2.5" y="5" width="15" height="10"/><path d="M2.5 5l7.5 6 7.5-6M2.5 15l5.5-5M17.5 15l-5.5-5"/>
          </svg>
        </span>
        marisol@rwofficepartners.com.au
      </li>
      <li class="contact">
        <span class="contact__icon">
          <svg viewBox="0 0 20 20" fill="none" stroke="#fff" stroke-width="1.3" stroke-linejoin="round">
            <path d="M5 3l3 3-1.6 2.2a9 9 0 0 0 5.4 5.4L14 12l3 3-2 2.2C9.5 17 3 10.5 2.8 5z"/>
          </svg>
        </span>
        61 487 902 346
      </li>
    </ul>
  </section>

</main>
</body>
</html>
```